12 Meter Banner-Design Lagerhalle
Zielgruppe
Wir errichten neue Elektroanlagen für Einfamilenhäuser und Wohnungen.
Hallo,
wir möchten auf 12 Meter drei Banner spannen um die unschönen Rohre und Kabel zu verdecken. Jeder der drei Banner soll 400cm breit und 160cm hoch werden.
-Banner 1 links: Motivationsspruch groß, mittig - : Wer immer tut, was er schon kann, bleibt immer das, was er schon ist.
- Banner 2 mitte : Komfortzone ( Grafiken habe ich im Anhang von dem Aufbau der Komfortzone ) Toll wäre ein selbst erstelltes Design passend zum Unternehmen / Farben Schriftart etc.
-Banner 3 rechts: Motivationsspruch : Zusammenkommen ist ein Beginn, zusammenbleiben ist ein Fortschritt, zusammenarbeiten ist ein Erfolg.
- Design nach Vorgabe Druckpilot ( Datasheet) erstellen
Gundsätzlich wäre super, wenn alle 3 Designs/ Banner miteinander harmonieren. Alles andere ist der Kreativität überlassen.
Schriftart: Fira Sans / Montserrat
Wir würden uns über eine Zusammenarbeit freuen.
Beste Grüße

```html
<!DOCTYPE html>
<html lang="de">
<head>
<meta charset="utf-8">
<title>Banner-Serie Lagerhalle – Kessler &amp; Brandt Elektrotechnik</title>
<link href="https://fonts.googleapis.com/css2?family=Montserrat:wght@500;600;700&family=Fira+Sans:wght@400;500&display=swap" rel="stylesheet">
<style>
  :root {
    --page: #e4e6e8;
    --banner: #ffffff;
    --ink: #1d1d1f;
    --quote-blue: #86bcd9;
    --brand-blue: #3d8fc4;
    --zone-outer: #9dc02f;
    --zone-ring: #e1ebb4;
    --zone-dark: #3a2a22;
    --zone-core: #e8852b;
    --vision-red: #d8262c;
  }
  * { box-sizing: border-box; margin: 0; padding: 0; }
  html, body { width: 846px; height: 1200px; overflow: hidden; }
  body { background: var(--page); font-family: "Montserrat", sans-serif; color: var(--ink); position: relative; }

  .banner {
    position: absolute; left: 30px; width: 786px; height: 314px;
    background: var(--banner); box-shadow: 0 2px 8px rgba(0,0,0,.12); overflow: hidden;
  }
  .banner--left { top: 64px; }
  .banner--middle { top: 443px; }
  .banner--right { top: 822px; }

  .quote-mark {
    position: absolute; font-family: "Montserrat", sans-serif; font-weight: 700;
    color: var(--quote-blue); font-size: 170px; line-height: 1; letter-spacing: -14px;
  }
  .quote-mark--open { left: 210px; top: 18px; }
  .quote-mark--close { right: 200px; bottom: -70px; }

  .quote-text {
    position: absolute; left: 0; right: 0; top: 58px; text-align: center;
    font-weight: 500; font-size: 40px; line-height: 46px;
  }
  .banner--right .quote-text { font-size: 36px; line-height: 44px; top: 56px; }

  .brand {
    position: absolute; right: 22px; bottom: 16px; display: flex; align-items: center; gap: 6px;
    font-family: "Montserrat", sans-serif; font-weight: 600; font-size: 11px;
    letter-spacing: .06em; color: var(--brand-blue); text-transform: uppercase;
  }
  .brand__dot { width: 14px; height: 14px; border-radius: 50%; background: var(--brand-blue); }

  .zone-chart { position: absolute; left: 0; top: 0; width: 786px; height: 314px; }
  .zone-chart text { font-family: "Fira Sans", sans-serif; }
</style>
</head>
<body>

  <section class="banner banner--left">
    <span class="quote-mark quote-mark--open">“</span>
    <p class="quote-text">Wer immer tut,<br>was er schon kann,<br>bleibt immer das,<br>was er schon ist.</p>
    <span class="quote-mark quote-mark--close">”</span>
    <div class="brand"><span class="brand__dot"></span>Kessler &amp; Brandt</div>
  </section>

  <section class="banner banner--middle">
    <svg class="zone-chart" viewBox="0 0 786 314" role="img" aria-label="Diagramm der Komfortzone mit Angstzone, Lernzone, Wachstumszone und Vision">
      <circle cx="300" cy="157" r="142" fill="var(--zone-outer)"/>
      <circle cx="300" cy="157" r="114" fill="var(--zone-ring)"/>
      <circle cx="290" cy="157" r="86" fill="var(--zone-dark)"/>
      <circle cx="270" cy="157" r="52" fill="var(--zone-core)"/>
      <line x1="322" y1="165" x2="640" y2="165" stroke="var(--vision-red)" stroke-width="2.5"/>
      <text x="270" y="161" text-anchor="middle" font-size="13" font-weight="500" fill="#fff">Komfortzone</text>
      <text x="348" y="160" text-anchor="middle" font-size="10" fill="#fff">Angstzone</text>
      <text x="396" y="160" text-anchor="middle" font-size="10" fill="var(--ink)">Lernzone</text>
      <text x="460" y="160" text-anchor="middle" font-size="10" fill="var(--ink)">Wachstumszone</text>
      <text x="612" y="158" text-anchor="middle" font-size="18" font-weight="500" fill="var(--ink)">Vision</text>
      <text x="300" y="92" text-anchor="middle" font-size="8" fill="#fff">Sicherheit</text>
      <text x="300" y="226" text-anchor="middle" font-size="8" fill="#fff">Kontrolle</text>
      <text x="340" y="110" text-anchor="middle" font-size="8" fill="#fff">Ausreden</text>
      <text x="340" y="210" text-anchor="middle" font-size="8" fill="#fff">Zweifel</text>
      <text x="300" y="60" text-anchor="middle" font-size="8" fill="var(--ink)">Neues lernen</text>
      <text x="300" y="260" text-anchor="middle" font-size="8" fill="var(--ink)">Probleme lösen</text>
      <text x="300" y="32" text-anchor="middle" font-size="8" fill="var(--ink)">Ziele setzen</text>
      <text x="300" y="290" text-anchor="middle" font-size="8" fill="var(--ink)">Träume leben</text>
    </svg>
    <div class="brand"><span class="brand__dot"></span>Kessler &amp; Brandt</div>
  </section>

  <section class="banner banner--right">
    <span class="quote-mark quote-mark--open">“</span>
    <p class="quote-text">Zusammenkommen ist ein Beginn,<br>zusammenbleiben ist ein Fortschritt,<br>zusammenarbeiten ist ein Erfolg.</p>
    <span class="quote-mark quote-mark--close">”</span>
    <div class="brand"><span class="brand__dot"></span>Kessler &amp; Brandt</div>
  </section>

</body>
</html>
```